Want to learn how to safely prescribe Testosterone, bio-identical hormones and become an expert? I can teach you in 1 weekend!
I have developed and designed Prime Vital Horizon: the worlds first complete Anti-Aging Medical Platform with a "one-stop-learn-workshop tier" where a medical provider can attend my 3-Day Modern Frontier Bright Years Renewal Seminar.
During the 3 days the medical provider will become an expert in:
1. Identifying, stratifying and qualifying the appropriate patient for the anti-age hormonal protocol
2. Prescribing Testosterone, Estrogen, Progesterone, Dhea, HcG HgH, both men and women, when appropriate, using my unique and proprietary medically supervised hormone optimization protocol (the protocol as long as my hormone book will be made available to all course attendants)
3. Understanding nutraceuticals and recommending them when appropriate. NovaPeakFORM, the most perfectly developed multi-vitamin, mineral and anti-oxidant pack on the market will be made available for all course attendants to try for free
4. Prescribing a complete and powerful medically optimized weight loss program backed by my proprietary medically supervised protocol and published book (both the protocol and book are available free to all course attendants)
5. Understanding the exercise challenge and understanding what kind of exercise should be prescribed, to whom and in what form. (an extensive proprietary video exercise video library will be available for all course attendants)
6. Upon completion of the workshop each attendee will be proficient enough that upon return to his/her office on Monday, he/she will be able to greatly increase his/her revenue with the knowledge learned.
7. Upon request, the attendee can remain on as affiliate physician of Prime Vital Horizon and learn directly from Dr Verhoeven who will help manage each affiliate physician's n.patient until the affiliate physician is confident enough on his/her own

The course will be held on a Saturday and Sunday in Hollywood Florida at the Coralview Lodge in sunny South Florida

The Course will begin at 930am and end at 3pm each day allowing ample time for sun and fun

I want the email to be STUNNING , to catch the eye of the doctor as this is who I will be sending it to, I want the doctor who opens this email to NOT trash it, to be hypnotized by it, to be intrigued by it, to go ahead and book this course!!!

I will include the logos of Prime Vital Horizon, NovaPeakForm and my weight loss book

Please keep in mind this email MUST be stunning!!! It will be emailed blindly solely to physicians who are notoriously busy and usually trash unknown emails.

I also need to be able to edit the template

Target Market(s)

Doctors

Industry/Entity Type

Medical

Font styles to use
Serif
Sans Serif
Decorative
Script

Colors

Designer to choose colors to be used in the design.

Requirements
Must have
• Stunning colors
• Catchy fonts
• Cool graphics
Nice to have
• an email that is not easily deleted!
• an email that hypnotizes the doctor
• an email that tells the doctor "this is the course I must take!!"
• and email that tells the doctor "if I dont take this course I am a fool"
Should not have
• Negative connotations

```html
<!DOCTYPE html>
<html lang="en">
<head>
<meta charset="utf-8">
<title>Prime Vital Horizon – Hormone Workshop</title>
<link href="https://fonts.googleapis.com/css2?family=Open+Sans:ital,wght@0,300;0,400;0,600;0,700;0,800;1,300;1,400;1,700&family=Great+Vibes&display=swap" rel="stylesheet">
<style>
  :root{
    --ink:#000;
    --white:#fff;
    --gold:#e8a300;
    --gold-bright:#f0a800;
    --bronze:#6f5000;
    --cream:#fdf6dd;
    --text-dark:#1e1e1e;
    --accent-red:#d8262b;
  }
  *{margin:0;padding:0;box-sizing:border-box}
  html,body{width:839px;height:1200px;overflow:hidden;background:var(--ink)}
  body{font-family:"Open Sans",Arial,sans-serif}
  .email{position:relative;width:839px;height:1200px;overflow:hidden;background:var(--ink)}

  .hero{position:absolute;left:0;top:0;width:839px;height:373px;background:var(--ink)}
  .hero-photo{position:absolute;left:20px;top:0;width:400px;height:373px;
    background:radial-gradient(ellipse 46% 60% at 50% 45%,#8a5a3c 0%,#4a2c1c 45%,#120a06 80%,#000 100%)}
  .hero-copy{position:absolute;left:428px;top:84px;color:var(--white)}
  .hero-question{font-weight:800;font-size:18.6px;line-height:21px;letter-spacing:-0.2px;text-transform:uppercase}
  .hero-script{font-family:"Great Vibes",cursive;color:var(--gold-bright);font-size:38px;line-height:42px;margin-top:2px}
  .hero-promise{margin-left:10px;margin-top:12px;font-weight:600;font-size:26.5px;line-height:30px;letter-spacing:0.3px}
  .hero-weekend{margin-left:10px;font-weight:800;font-size:41px;line-height:44px;color:var(--gold-bright);letter-spacing:-0.3px}

  .intro{position:absolute;left:0;top:373px;width:839px;height:143px;background:var(--bronze);
    padding:34px 50px 0 63px;color:var(--white);font-weight:700;font-size:15.4px;line-height:18.4px;text-transform:uppercase}

  .curriculum{position:absolute;left:0;top:516px;width:839px;height:489px;background:var(--gold);padding:37px 50px 0 0}
  .curriculum-title{margin-left:81px;font-weight:600;font-size:16.2px;line-height:20px;color:var(--text-dark);text-transform:uppercase}
  .curriculum-list{list-style:none;margin-top:10px}
  .curriculum-list li{position:relative;padding-left:81px;font-weight:300;font-size:14.4px;line-height:16.8px;color:var(--text-dark);margin-bottom:8px}
  .curriculum-list .num{position:absolute;left:63px;top:0;font-weight:700}

  .details{position:absolute;left:0;top:1005px;width:420px;height:182px;background:var(--cream);padding:30px 20px 0 36px;color:#333}
  .details-venue{font-style:italic;font-weight:300;font-size:13.5px;line-height:16.5px}
  .details-venue b{font-weight:700}
  .details-label{margin-top:22px;font-weight:700;font-size:13.5px;letter-spacing:0.3px}
  .details-time{margin-top:4px;font-weight:300;font-size:13.5px;line-height:16.5px}

  .brands{position:absolute;left:420px;top:1005px;width:419px;height:182px;background:var(--white)}
  .brand{position:absolute;display:flex;align-items:center;gap:8px;font-weight:700;color:var(--accent-red)}
  .brand-supplement{left:42px;top:44px;font-size:19px}
  .brand-platform{left:42px;top:126px;font-size:21px}
  .brand-mark{width:14px;height:14px;border-radius:50%;background:var(--accent-red)}
  .book-cover{position:absolute;left:302px;top:29px;width:82px;height:117px;
    background:linear-gradient(160deg,#b5773e 0%,#3a2414 55%,#8a5a32 100%);border:2px solid #c98a4a}
  .book-label{position:absolute;left:296px;top:150px;width:94px;text-align:center;font-weight:800;font-size:8.5px;letter-spacing:0.4px;color:#111}

  .footer-strip{position:absolute;left:0;top:1187px;width:839px;height:13px;background:var(--ink)}
</style>
</head>
<body>
<main class="email">

  <header class="hero">
    <div class="hero-photo" role="img" aria-label="Fit woman in black sportswear holding two dumbbells, shown from chest to thighs"></div>
    <div class="hero-copy">
      <h1 class="hero-question">Want to learn how to<br>safely prescribe testosterone,<br>bio-identical hormones and</h1>
      <p class="hero-script">Become an Expert?</p>
      <p class="hero-promise">I CAN TEACH YOU</p>
      <p class="hero-weekend">IN 1 WEEKEND!</p>
    </div>
  </header>

  <section class="intro">
    I have developed and designed Prime Vital Horizon: the worlds first complete anti-aging medical platform with a "one-stop-learn-workshop tier" where a medical provider can attend my 3-Day Modern Frontier Bright Years Renewal Seminar.
  </section>

  <section class="curriculum">
    <h2 class="curriculum-title">During the 3 days the medical provider will become an expert in:</h2>
    <ol class="curriculum-list">
      <li><span class="num">1</span>Identifying, stratifying and qualifying the appropriate patient for the anti-age hormonal protocol</li>
      <li><span class="num">2</span>Prescribing Testosterone, Estrogen, Progesterone, Dhea, HcG HgH, both men and women, when appropriate, using my unique and proprietary medically supervised hormone optimization protocol (the protocol as long as my hormone book will be made available to all course attendants)</li>
      <li><span class="num">3</span>Understanding nutraceuticals and recommending them when appropriate. NovaPeakFORM, the most perfectly developed multi-vitamin, mineral and anti-oxidant pack on the market will be made available for all course attendants to try for free</li>
      <li><span class="num">4</span>Prescribing a complete and powerful medically optimized weight loss program backed by my proprietary medically supervised protocol and published book (both the protocol and book are available free to all course attendants)</li>
      <li><span class="num">5</span>Understanding the exercise challenge and understanding what kind of exercise should be prescribed, to whom and in what form. (an extensive proprietary video exercise video library will be available for all course attendants)</li>
      <li><span class="num">6</span>Upon completion of the workshop each attendee will be proficient enough that upon return to his/her office on Monday, he/she will be able to greatly increase his/her revenue with the knowledge learned.</li>
      <li><span class="num">7</span>Upon request, the attendee can remain on as affiliate physician of Prime Vital Horizon and learn directly from Dr Verhoeven who will help manage each affiliate physician's n.patient until the affiliate physician is confident enough on his/her own.</li>
    </ol>
  </section>

  <section class="details">
    <p class="details-venue">The course will be held on a <b>Saturday</b> and <b>Sunday</b> in <b>Hollywood Florida</b> at the Coralview Lodge in sunny South Florida</p>
    <p class="details-label">TIMING:</p>
    <p class="details-time">begin at 930am and end at 3pm<br>each day allowing ample time for sun and fun</p>
  </section>

  <aside class="brands">
    <div class="brand brand-supplement"><span class="brand-mark"></span>NovaPeakForm</div>
    <div class="brand brand-platform">Prime Vital Horizon</div>
    <div class="book-cover" role="img" aria-label="Cover of the weight loss book showing a slim woman in black"></div>
    <p class="book-label">AVAILABLE NOW!</p>
  </aside>

  <div class="footer-strip"></div>
</main>
</body>
</html>
```